Poster Design for SMCL 2026 – Fitness + Live-Fire Competition

Design a clean, minimalist event poster for The Steady Mark Classic (SMCL 2026) - Puerto Rico’s first Fitness + Live-Fire competition.

The poster will be printed (11×17, portrait) and placed in gyms, shooting ranges, and athletic spaces, so it must communicate clearly in 3-5 seconds and feel credible, professional, and intentional.
This is not a flashy LiftRally or tactical/military flyer.
The tone should be calm, confident, and premium.

** Required Content & Hierarchy **

** Main title (largest element) **
THE
STEADY MARK
PUERTO RICO

** Subtitle **
Puerto Rico’s first
Fitness + Live-Fire competition

Divisions (clear and readable)
Pistol & Pistol + Rifle
Scale | Beginner | Intermediate

Date:
March 7, 2026

** Imagery **
- Use the provided photo of athletes standing in a line holding pistols and kettlebells as the primary visual.
- Image should feel controlled and safe, not aggressive
- Can be full-bleed or centered, but must not overpower the text

** QR Code (conversion element) **
- A QR code will be provided.
- Place at the bottom center or bottom right
- Include CTA: SCAN TO REGISTER
QR should be large and easy to scan

** Pictavo (secondary action) **
- Include a small Pictavo logo and the handle:
@thesmcl

** Placement **
- Right side or bottom area
- Secondary to the QR code
- Should not compete with the main title

** Purpose **
- Allows people to follow and learn more online
- Not the primary call to action (QR → registration is primary)

** Style Direction **
- Minimalist
- High contrast
- Limited color palette (black, white, muted tones)
- Strong typography, plenty of negative space

** Avoid **
- Overcrowded layouts
- Emojis
- Loud colors
- Military or gun-culture clichés

** Deliverables **
- Print-ready poster (11×17, portrait)
- Editable source file (Illustrator preferred)
- High-resolution PDF for print
- Digital version for Pictavo

** Success Criteria **
Someone should immediately understand:
- What the event is
- That it’s legitimate and well-organized
- That it’s open to different experience levels
- That they should scan the QR or follow @thesmcl

```html
<!DOCTYPE html>
<html lang="en">
<head>
<meta charset="utf-8">
<title>The Steady Mark Classic – Poster</title>
<link href="https://fonts.googleapis.com/css2?family=Poppins:wght@400;600;700;800;900&display=swap" rel="stylesheet">
<style>
  :root {
    --backdrop: #ececec;
    --brown: #8a5f36;
    --tan: #c9a27a;
    --dark: #3a2314;
    --white: #ffffff;
    --sky: #a9c9e4;
    --foliage: #55703f;
    --shade: #3e3a2c;
  }
  * { margin: 0; padding: 0; box-sizing: border-box; }
  html, body {
    width: 1200px; height: 1200px; overflow: hidden;
    background: var(--backdrop);
    font-family: "Poppins", sans-serif;
  }
  .poster {
    position: absolute; left: 250px; top: 60px;
    width: 700px; height: 1080px;
    background: var(--brown);
    overflow: hidden;
    color: var(--white);
  }
  .hero-photo {
    position: absolute; left: 0; top: 0; width: 700px; height: 520px;
    background:
      linear-gradient(to bottom, rgba(138,95,54,0) 0%, rgba(138,95,54,0) 45%, var(--brown) 92%),
      linear-gradient(to bottom, var(--sky) 0%, #c9dbe8 9%, var(--foliage) 18%, #6f7f4a 40%, var(--shade) 62%, #5a4a33 80%);
  }
  .title-art {
    position: absolute; left: 0; top: 0; width: 700px; height: 1080px;
    font-family: "Poppins", sans-serif;
  }
  .title-the { fill: var(--white); font-weight: 900; }
  .title-name { fill: var(--tan); font-weight: 800; stroke: var(--white); stroke-width: 1.5; paint-order: stroke; }
  .title-region { fill: var(--white); font-weight: 800; }
  .title-region-lg { fill: var(--dark); font-weight: 800; stroke: var(--white); stroke-width: 2; paint-order: stroke; }
  .subtitle {
    position: absolute; left: 72px; top: 686px;
    font-size: 24px; line-height: 30px; font-weight: 400;
  }
  .accent-bar {
    position: absolute; left: 518px; top: 706px; width: 112px; height: 19px;
    background: linear-gradient(to right, rgba(58,35,20,0), var(--dark) 60%);
  }
  .divisions { position: absolute; left: 72px; top: 796px; }
  .divisions-types { font-size: 26px; font-weight: 700; line-height: 34px; }
  .divisions-levels { font-size: 19px; font-weight: 400; line-height: 26px; }
  .event-mark {
    position: absolute; left: 546px; top: 793px; width: 84px; height: 84px;
    border-radius: 50%; background: var(--dark);
    display: flex; align-items: center; justify-content: center;
    font-size: 17px; font-weight: 700; color: var(--white);
  }
  .event-date { position: absolute; left: 72px; top: 904px; }
  .date-day { font-size: 46px; font-weight: 400; line-height: 52px; }
  .date-year { font-size: 68px; font-weight: 800; line-height: 66px; color: var(--dark); }
  .footer-bar {
    position: absolute; left: 72px; top: 1044px; width: 341px; height: 16px;
    background: var(--dark);
  }
  .cta { position: absolute; right: 70px; top: 958px; text-align: right; }
  .cta-label { font-size: 18px; line-height: 26px; font-weight: 400; }
  .cta-handle {
    font-size: 18px; line-height: 28px; font-weight: 400;
    display: flex; align-items: center; justify-content: flex-end; gap: 10px;
  }
  .handle-dot {
    width: 18px; height: 18px; border-radius: 50%;
    border: 2px solid var(--white);
  }
</style>
</head>
<body>
  <main class="poster">
    <div class="hero-photo" role="img" aria-label="Athletes in plate carriers and ear protection standing in a line on a grassy range, aiming pistols under a blue sky"></div>

    <svg class="title-art" viewBox="0 0 700 1080" width="700" height="1080" aria-label="The Steady Mark Puerto Rico">
      <text class="title-the" x="124" y="665" font-size="74" transform="rotate(-90 124 665)" textLength="336" lengthAdjust="spacingAndGlyphs">THE</text>
      <text class="title-name" x="225" y="395" font-size="94" textLength="407" lengthAdjust="spacingAndGlyphs">STEADY</text>
      <text class="title-name" x="225" y="452" font-size="81" textLength="407" lengthAdjust="spacingAndGlyphs">MARK</text>
      <text class="title-region" x="225" y="533" font-size="107" textLength="407" lengthAdjust="spacingAndGlyphs">PUERTO</text>
      <text class="title-region-lg" x="225" y="665" font-size="170" textLength="407" lengthAdjust="spacingAndGlyphs">RICO</text>
    </svg>

    <p class="subtitle">Puerto Rico’s first<br>Fitness + Live-Fire competition</p>
    <div class="accent-bar"></div>

    <section class="divisions">
      <p class="divisions-types">Pistol &amp; Pistol + Rifle</p>
      <p class="divisions-levels">Scale | Beginner | Intermediate</p>
    </section>

    <div class="event-mark">SMCL</div>

    <section class="event-date">
      <p class="date-day">March 7</p>
      <p class="date-year">2026</p>
    </section>

    <div class="footer-bar"></div>

    <section class="cta">
      <p class="cta-label">Scan To Register</p>
      <p class="cta-handle"><span class="handle-dot"></span>@thesmcl</p>
    </section>
  </main>
</body>
</html>
```